Business Card Design Project

Tarvolink - based in Melbourne, Australia. We plan, design, implement and support network infrastructure (Plemba, Hollvask, Q8, Stormpike etc).

Target Market(s)

Small/Medium enterprise and Corporate.

Industry/Entity Type

Business

```html
<!DOCTYPE html>
<html lang="en">
<head>
<meta charset="utf-8">
<title>Tarvolink Business Card</title>
<link rel="stylesheet" href="https://fonts.googleapis.com/css2?family=Open+Sans:wght@400;600;700&display=swap">
<style>
:root{
  --bg:#e9e6e1;
  --ink:#1f1f1f;
  --ink-2:#2c2c2c;
  --paper:#ffffff;
  --gold:#e9a72b;
  --grey:#8f9092;
  --light:#e8e8e8;
}
*{margin:0;padding:0;box-sizing:border-box}
html,body{width:1200px;height:886px;overflow:hidden;background:var(--bg);font-family:"Open Sans",Arial,sans-serif}
.stage{position:relative;width:1200px;height:886px}
.card{position:absolute;top:293px;width:540px;height:300px;border-radius:12px;overflow:hidden;box-shadow:0 6px 18px rgba(0,0,0,.18)}
.card--front{left:40px;background:var(--paper)}
.card--back{left:620px;background:linear-gradient(135deg,var(--ink-2),#151515 60%,#2a2a2a)}
.front-top{position:absolute;left:0;top:0;width:100%;height:112px;background:var(--paper);display:flex;align-items:center;padding-left:46px;gap:14px}
.brand-dot{width:46px;height:46px;border-radius:50%;background:var(--grey)}
.brand-name{font-weight:700;font-size:46px;color:var(--grey);letter-spacing:-1px}
.tagline-band{position:absolute;left:0;top:112px;width:100%;height:20px;background:var(--gold);color:var(--paper);font-size:10.5px;line-height:20px;padding-left:46px}
.front-body{position:absolute;left:0;top:132px;width:100%;height:168px;background:linear-gradient(160deg,#2e2e2e,var(--ink) 55%)}
.person{position:absolute;left:46px;top:20px}
.person-name{color:var(--gold);font-weight:600;font-size:20px;letter-spacing:.3px}
.person-role{color:var(--paper);font-weight:700;font-size:11.5px;margin-top:1px}
.divider{position:absolute;left:268px;top:22px}
.contacts{position:absolute;list-style:none;color:var(--light);font-size:11.5px}
.contacts li{display:flex;align-items:flex-start;gap:9px;margin-bottom:6px;line-height:1.35}
.contacts svg{flex:none;margin-top:2px}
.contacts--place{left:314px;top:18px}
.contacts--direct{left:46px;top:92px}
.back-logo{position:absolute;inset:0;display:flex;align-items:center;justify-content:center;gap:14px}
.back-logo .brand-dot{background:var(--grey)}
.back-logo .brand-name{color:var(--gold);font-size:44px}
</style>
</head>
<body>
<main class="stage">
  <section class="card card--front">
    <div class="front-top">
      <span class="brand-dot"></span>
      <span class="brand-name">Tarvolink</span>
    </div>
    <div class="tagline-band">We plan, design, implement and support network infrastructure</div>
    <div class="front-body">
      <div class="person">
        <div class="person-name">MARLEN OSTROW</div>
        <div class="person-role">Managing Director</div>
      </div>
      <svg class="divider" width="30" height="44" viewBox="0 0 30 44"><line x1="4" y1="2" x2="26" y2="42" stroke="#ffffff" stroke-width="1.4"/></svg>
      <ul class="contacts contacts--place">
        <li>
          <svg width="10" height="13" viewBox="0 0 10 13"><path d="M5 0a5 5 0 0 0-5 5c0 3.5 5 8 5 8s5-4.5 5-8a5 5 0 0 0-5-5z" fill="#e9a72b"/><circle cx="5" cy="5" r="1.8" fill="#1f1f1f"/></svg>
          <span>Tarvolink Pty Ltd 14 Keel Lane<br>Carlton, VIC 3053</span>
        </li>
        <li>
          <svg width="11" height="11" viewBox="0 0 12 12"><circle cx="6" cy="6" r="5.5" fill="#e9a72b"/><path d="M0.5 6h11M6 .5c-3 3-3 8 0 11M6 .5c3 3 3 8 0 11" stroke="#1f1f1f" stroke-width="1" fill="none"/></svg>
          <span>www.tarvolink-net.com</span>
        </li>
      </ul>
      <ul class="contacts contacts--direct">
        <li>
          <svg width="11" height="11" viewBox="0 0 12 12"><path d="M2 0h3l1 3-2 1.5a7 7 0 0 0 3.5 3.5L9 6l3 1v3a2 2 0 0 1-2 2A10 10 0 0 1 0 2a2 2 0 0 1 2-2z" fill="#e9a72b"/></svg>
          <span>+XX XXXX XXXX</span>
        </li>
        <li>
          <svg width="12" height="11" viewBox="0 0 12 11"><rect x="3" y="0" width="6" height="3" fill="#e9a72b"/><rect x="0" y="3.5" width="12" height="5" rx="1" fill="#e9a72b"/><rect x="3" y="7" width="6" height="4" fill="#e9a72b" stroke="#1f1f1f" stroke-width=".8"/></svg>
          <span>+XX XXXX XXXX</span>
        </li>
        <li>
          <svg width="12" height="9" viewBox="0 0 12 9"><rect width="12" height="9" fill="#e9a72b"/><path d="M0 0l6 5 6-5" stroke="#1f1f1f" stroke-width="1" fill="none"/></svg>
          <span>info@tarvolink-net.com</span>
        </li>
      </ul>
    </div>
  </section>

  <section class="card card--back">
    <div class="back-logo">
      <span class="brand-dot"></span>
      <span class="brand-name">Tarvolink</span>
    </div>
  </section>
</main>
</body>
</html>
```